KM PowerPoint Design

I need a slick PowerPoint template following my newly designed logo (see the attached ZIP file for logo details, fonts, and colors).
Please also see the Sample.pptx file for an idea of the simplicity and slickness I am after (do not consider the colors or fonts from the Sample file, just as an idea). Other ideas are very welcome.

```html
<!DOCTYPE html>
<html lang="en">
<head>
<meta charset="utf-8">
<title>KM PowerPoint Template</title>
<link href="https://fonts.googleapis.com/css2?family=Montserrat:wght@400;500;600;700;800&display=swap" rel="stylesheet">
<style>
  :root {
    --blue: #1f3a9c;
    --ink: #1c2033;
    --paper: #ffffff;
    --canvas: #e9e9ea;
    --muted: #2b2f45;
  }
  * { margin: 0; padding: 0; box-sizing: border-box; }
  html, body { width: 1200px; height: 524px; overflow: hidden; }
  body { background: var(--canvas); font-family: "Montserrat", sans-serif; color: var(--ink); position: relative; }

  .slide { position: absolute; width: 343px; height: 193px; background: var(--paper); overflow: hidden;
           box-shadow: 0 14px 18px -10px rgba(0,0,0,.28); }
  .slide--cover { left: 47px; top: 65px; }
  .slide--welcome { left: 428px; top: 65px; }
  .slide--services { left: 798px; top: 65px; }
  .slide--title { left: 47px; top: 280px; }
  .slide--split { left: 428px; top: 280px; }
  .slide--contact { left: 798px; top: 280px; }

  .photo, .abs { position: absolute; }

  .heading { font-weight: 600; font-size: 15px; line-height: 1.1; color: var(--ink); }
  .heading strong { display: block; font-weight: 700; color: var(--blue); }
  .body { font-size: 5.6px; line-height: 1.4; color: var(--muted); }
  .item-title { font-size: 5.6px; font-weight: 700; color: var(--ink); margin-bottom: 1px; }
  .item-text { font-size: 5.4px; line-height: 1.35; color: var(--muted); }
  .on-blue, .on-blue .item-title, .on-blue .item-text, .on-blue .body { color: #fff; }

  .brand-name { font-weight: 700; font-size: 11px; letter-spacing: .5px; text-align: center; }

  /* cover */
  .cover-photo { inset: 0; background: linear-gradient(120deg, #2c2f78 0%, #3b4190 45%, #2e3377 100%); }
  .cover-title { width: 100%; top: 64px; text-align: center; color: #fff; font-weight: 700; font-size: 24px; letter-spacing: .3px; }
  .cover-sub { width: 100%; top: 110px; text-align: center; color: #fff; font-weight: 700; font-size: 6.5px; letter-spacing: 1.4px; }
  .cover-brand { width: 100%; top: 145px; color: #fff; }

  /* welcome */
  .welcome-photo { left: 0; top: 0; width: 128px; height: 193px; background: linear-gradient(160deg, #ede9e4 0%, #d8d2cb 60%, #b9aea5 100%); }
  .welcome-heading { left: 211px; top: 38px; }
  .welcome-box { left: 132px; top: 93px; width: 187px; height: 70px; background: var(--blue); padding: 6px 8px; }

  /* services */
  .tile { position: absolute; width: 108px; height: 96px; }
  .tile--blue { background: var(--blue); }
  .tile--top { padding: 13px 10px 0 26px; }
  .tile--bottom { padding: 42px 8px 0 31px; }
  .tile--photo { background: linear-gradient(180deg, #e6e6e6, #b9b9bb); }
  .services-heading { left: 234px; top: 47px; }
  .services-body { left: 234px; top: 82px; width: 104px; }

  /* title slide */
  .title-photo { left: 0; top: 0; width: 192px; height: 193px; background: linear-gradient(135deg, #cfd6dd 0%, #8aa0b7 55%, #2d4aa6 100%); }
  .list { display: flex; flex-direction: column; gap: 9px; }
  .title-heading { left: 216px; top: 25px; }
  .title-list { left: 216px; top: 70px; width: 112px; }

  /* split */
  .split-photo { left: 0; top: 0; width: 107px; height: 160px; background: linear-gradient(160deg, #6f8f5a 0%, #9fb4a5 45%, #c8c3b6 100%); }
  .split-box { left: 79px; top: 20px; width: 98px; height: 125px; background: var(--blue); padding: 14px 8px; }
  .split-box .heading { color: #fff; font-size: 13px; font-weight: 700; }
  .split-box .body { font-size: 4.4px; margin-top: 10px; }
  .split-list { left: 200px; top: 43px; width: 130px; }

  /* contact */
  .contact-panel { left: 0; top: 0; width: 182px; height: 193px; background: var(--blue); padding: 47px 0 0 33px; }
  .contact-panel h2 { font-size: 11px; font-weight: 700; color: #fff; margin-bottom: 8px; }
  .contact-panel .list { gap: 7px; }
  .contact-panel .item-title { font-size: 7px; font-weight: 500; }
  .contact-photo-a { left: 140px; top: 0; width: 85px; height: 138px; background: linear-gradient(170deg, #7d98b6 0%, #a7b8c4 50%, #8d8a87 100%); }
  .contact-photo-b { left: 229px; top: 0; width: 114px; height: 138px; background: linear-gradient(170deg, #b7a58d 0%, #9c8f86 50%, #3a3b44 100%); }
  .contact-brand { left: 182px; width: 161px; top: 159px; color: var(--blue); }
</style>
</head>
<body>

<section class="slide slide--cover">
  <div class="photo cover-photo" role="img" aria-label="Business team in front of an office building, blue tinted"></div>
  <h1 class="abs cover-title">YOUR TITLE HERE</h1>
  <p class="abs cover-sub">POWERPOINT PRESENTATION</p>
  <p class="abs brand-name cover-brand">KM</p>
</section>

<section class="slide slide--welcome">
  <div class="photo welcome-photo" role="img" aria-label="Smiling woman in shirt and tie holding a stack of books"></div>
  <h2 class="abs heading welcome-heading">Welcome <strong>Massage</strong></h2>
  <div class="abs welcome-box on-blue">
    <p class="body">Lorem ipsum dolor sit amet, cons ectetuer adipiscing elit, sed diam nonummy nibh euismod tincidunt ut laoreet dolore magna aliquam erat volutpat. Ut wisi enim ad minim veniam, sed diam nonummy nibh euismod tincidunt ut laoreet dolore. orem ipsum dolor sit amet, cons ectetuer adipiscing elit, sed diam nonummy nibh euismod tincidunt ut.</p>
  </div>
</section>

<section class="slide slide--services">
  <div class="tile tile--blue tile--top on-blue" style="left:0;top:0;">
    <p class="item-title">YOUR TITLE HERE</p>
    <p class="item-text">Lorem ipsum dolor sit amet. Ut wisi enim ad minim veniam.</p>
  </div>
  <div class="tile tile--photo" style="left:108px;top:0;" role="img" aria-label="Stacked books with glasses on top"></div>
  <div class="tile tile--photo" style="left:0;top:96px;" role="img" aria-label="Open books standing in a row"></div>
  <div class="tile tile--blue tile--bottom on-blue" style="left:108px;top:96px;">
    <p class="item-title">YOUR TITLE HERE</p>
    <p class="item-text">Lorem ipsum dolor sit amet. Ut wisi enim ad minim veniam.</p>
  </div>
  <h2 class="abs heading services-heading">Our Main <strong>Services</strong></h2>
  <p class="abs body services-body">Lorem ipsum dolor sit amet, cons ectetuer adipiscing elit, sed diam nonummy nibh euismod tincidunt ut laoreet dolore magna aliquam erat volutpat. Ut wisi enim ad minim veniam, sed diam nonummy nibh euismod tincidunt ut laoreet dolore.</p>
</section>

<section class="slide slide--title">
  <div class="photo title-photo" role="img" aria-label="Woman in blue sweater holding a tablet with charts"></div>
  <h2 class="abs heading title-heading">Your title <strong>goes here</strong></h2>
  <div class="abs list title-list">
    <div><p class="item-title">YOUR TITLE HERE</p><p class="item-text">Lorem ipsum dolor sit amvolutpat. Ut wisi enim ad minim veniam.</p></div>
    <div><p class="item-title">YOUR TITLE HERE</p><p class="item-text">Lorem ipsum dolor sit amvolutpat. Ut wisi enim ad minim veniam.</p></div>
    <div><p class="item-title">YOUR TITLE HERE</p><p class="item-text">Lorem ipsum dolor sit amvolutpat. Ut wisi enim ad minim veniam.</p></div>
  </div>
</section>

<section class="slide slide--split">
  <div class="photo split-photo" role="img" aria-label="Student holding a blue folder outside a building"></div>
  <div class="abs split-box on-blue">
    <h2 class="heading">Title<br>Here</h2>
    <p class="body">Lorem ipsum dolor sit amet, cons ectetuer adipiscing elit, sed diam nonummy nibh euismod tincidunt ut laoreet dolore magna aliquam erat volutpat. Ut wisi enim ad minim veniam.</p>
  </div>
  <div class="abs list split-list">
    <div><p class="item-title">YOUR TITLE HERE</p><p class="item-text">Lorem ipsum dolor sit amvolutpat. Ut wisi enim ad minim veniam.</p></div>
    <div><p class="item-title">YOUR TITLE HERE</p><p class="item-text">Lorem ipsum dolor sit amvolutpat. Ut wisi enim ad minim veniam.</p></div>
    <div><p class="item-title">YOUR TITLE HERE</p><p class="item-text">Lorem ipsum dolor sit amvolutpat. Ut wisi enim ad minim veniam.</p></div>
  </div>
</section>

<section class="slide slide--contact">
  <div class="abs contact-panel on-blue">
    <h2>CONTACT</h2>
    <div class="list">
      <div><p class="item-title">Location</p><p class="item-text">Lorem ipsum dolor sit<br>amet, cons diamnonummy.</p></div>
      <div><p class="item-title">Phone Number</p><p class="item-text">Lorem ipsum dolor sit<br>amet, cons diamnonummy.</p></div>
      <div><p class="item-title">Website</p><p class="item-text">Lorem ipsum dolor sit<br>amet, cons diamnonummy.</p></div>
    </div>
  </div>
  <div class="photo contact-photo-a" role="img" aria-label="Student with blue folder by a glass building"></div>
  <div class="photo contact-photo-b" role="img" aria-label="Group of business people standing with arms crossed"></div>
  <p class="abs brand-name contact-brand">KM</p>
</section>

</body>
</html>
```